The Plaster & Resonance Craftworks Inc (PRCI)

Create a LOGO and Business Card design.

Colors: Black, Bright Yellow & Red

Description of company: commercial carpentry, metal framing, drywall, taping/spackling, demolition, rough/finish carpentry.

Target Market(s)

developers, architects, general contractors, construction managers

Industry/Entity Type

Business

```html
<!DOCTYPE html>
<html lang="en">
<head>
<meta charset="UTF-8">
<title>PRCI Business Cards</title>
<link rel="stylesheet" href="https://fonts.googleapis.com/css2?family=Oswald:wght@300;400;700&display=swap">
<style>
  :root {
    --backdrop: #7a4f2c;
    --card-black: #050505;
    --brand-red: #d4141a;
    --bright-yellow: #f3e51a;
    --rule-grey: #3a3a3a;
  }
  * { margin: 0; padding: 0; box-sizing: border-box; }
  html, body { width: 900px; height: 1200px; overflow: hidden; }
  body {
    background: var(--backdrop);
    font-family: "Oswald", sans-serif;
    position: relative;
  }
  .card {
    position: absolute;
    left: 135px;
    width: 630px;
    height: 380px;
    background: var(--card-black);
    box-shadow: 0 10px 24px rgba(0,0,0,0.45);
    color: var(--bright-yellow);
    text-align: center;
  }
  .card--front { top: 170px; }
  .card--back { top: 640px; }

  .measure-rule {
    position: absolute;
    top: 48px;
    left: 60px;
    width: 510px;
    height: 14px;
  }

  .wordmark {
    display: inline-flex;
    align-items: center;
    gap: 14px;
    color: var(--brand-red);
    font-weight: 700;
    letter-spacing: 6px;
    line-height: 1;
  }
  .wordmark__square {
    background: var(--brand-red);
    display: inline-block;
  }
  .card--front .wordmark { margin-top: 120px; font-size: 78px; }
  .card--front .wordmark__square { width: 22px; height: 22px; }
  .card--back .wordmark { margin-top: 48px; font-size: 48px; }
  .card--back .wordmark__square { width: 14px; height: 14px; }

  .tagline {
    margin-top: 34px;
    font-weight: 400;
    font-size: 26px;
    letter-spacing: 0.3px;
  }
  .contact {
    margin-top: 24px;
    font-weight: 400;
    font-size: 26px;
    line-height: 1.3;
  }
  .web {
    margin-top: 44px;
    font-weight: 400;
    font-size: 26px;
  }
</style>
</head>
<body>
  <section class="card card--front">
    <svg class="measure-rule" viewBox="0 0 510 14" aria-hidden="true">
      <line x1="0" y1="13" x2="510" y2="13" stroke="#3a3a3a" stroke-width="1"/>
      <g stroke="#3a3a3a" stroke-width="1">
        <line x1="0" y1="0" x2="0" y2="13"/><line x1="51" y1="5" x2="51" y2="13"/>
        <line x1="102" y1="0" x2="102" y2="13"/><line x1="153" y1="5" x2="153" y2="13"/>
        <line x1="204" y1="0" x2="204" y2="13"/><line x1="255" y1="5" x2="255" y2="13"/>
        <line x1="306" y1="0" x2="306" y2="13"/><line x1="357" y1="5" x2="357" y2="13"/>
        <line x1="408" y1="0" x2="408" y2="13"/><line x1="459" y1="5" x2="459" y2="13"/>
        <line x1="510" y1="0" x2="510" y2="13"/>
      </g>
    </svg>
    <div class="wordmark"><span class="wordmark__square"></span>PRCI</div>
    <p class="tagline">The Plaster &amp; Resonance Craftworks Inc.</p>
  </section>

  <section class="card card--back">
    <div class="wordmark"><span class="wordmark__square"></span>PRCI</div>
    <p class="contact">2470 Linden/Riverton Ohio/45210<br>Call us: (555)214-0389</p>
    <p class="web">Visit us online at: prci-works.com</p>
  </section>
</body>
</html>
```